・電子書籍の表紙デザインをお願いします。

・本の内容
モヤモヤグルグルしてるただの主婦でも、天職につながれば稼げるようになる。
自分の事を理解し天職につながることによって、
自信や人間関係やお金、仕事や健康までも、うまく回り始める。
私のエピソードから天職につながるプロセスを見てもらって解説してます。
後半で、あなたの天職につながるワークを実践して
スモールステップを踏み出せるようになるという内容になっています。

・デザイン要望
文字を大きく、パッと見て何が書いてあるかわかりやすいようにして欲しいです。

その他何かありましたら、気軽に質問して下さいね。
よろしくお願いいたします。

タイトルとして

スル~っととんとん拍子に
『ひらめく毎日!をひらく本』
モヤモヤグルグルしてたただの主婦の私が、
まさかの経営者になった理由
森川遥香

読者限定プレゼント
「何かしたい」でも「何をしたいのかわからない」
そんなあなたに
「星読みカルテ」プレゼント

入れて欲しいです。
とんとん拍子 → トントン拍子

軽快なイメージに一番近かったです。

皆さんのご提案、すべて素敵で迷いました。
ありがとうございました。

```html
<!DOCTYPE html>
<html lang="ja">
<head>
<meta charset="utf-8">
<title>ひらめく毎日!をひらく本</title>
<link rel="stylesheet" href="https://fonts.googleapis.com/css2?family=M+PLUS+Rounded+1c:wght@800;900&family=Noto+Sans+JP:wght@500;700;900&display=swap">
<style>
  :root {
    --pink: #ef9f9b;
    --pink-deep: #e9817f;
    --blue: #4f93b8;
    --blue-light: #86bcd6;
    --yellow: #ffe600;
    --white: #ffffff;
    --accent-red: #e8555f;
    --title-shadow: rgba(160, 60, 60, 0.35);
  }
  * { margin: 0; padding: 0; box-sizing: border-box; }
  html, body { width: 749px; height: 1200px; overflow: hidden; }
  body { font-family: "Noto Sans JP", sans-serif; background: var(--pink); }

  .cover {
    position: relative;
    width: 749px;
    height: 1200px;
    overflow: hidden;
    color: var(--white);
  }
  .cover-photo {
    position: absolute; inset: 0;
    background:
      radial-gradient(ellipse at 70% 55%, rgba(222, 190, 150, 0.55) 0%, rgba(222, 190, 150, 0) 45%),
      linear-gradient(170deg, var(--pink) 0%, var(--pink) 52%, var(--pink-deep) 62%, var(--blue-light) 78%, var(--blue) 100%);
  }

  .tagline {
    position: absolute; left: 70px; top: 42px;
    font-family: "M PLUS Rounded 1c", sans-serif; font-weight: 900;
    font-size: 52px; line-height: 1; letter-spacing: 1px;
    text-shadow: 0 3px 6px var(--title-shadow);
  }
  .tagline .hl { color: var(--yellow); }
  .tagline .small { font-size: 42px; }

  .title {
    position: absolute; left: 34px; top: 125px;
    font-weight: 900; font-size: 96px; line-height: 1.1; letter-spacing: -2px;
    text-shadow: 0 4px 10px var(--title-shadow);
    white-space: nowrap;
  }
  .subtitle {
    position: absolute; left: 72px; top: 295px;
    font-weight: 900; font-size: 50px; line-height: 1.2;
    text-shadow: 0 3px 6px var(--title-shadow);
  }

  .lead {
    position: absolute; left: 70px; top: 462px;
    font-weight: 700; font-size: 30px; line-height: 45px;
  }
  .lead .hl { color: var(--yellow); }
  .author {
    position: absolute; left: 72px; top: 655px;
    font-weight: 700; font-size: 28px; letter-spacing: 2px;
  }

  .gift-badge {
    position: absolute; left: 560px; top: 756px;
    width: 188px; height: 188px; border-radius: 50%;
    background: var(--white);
    display: flex; flex-direction: column; align-items: center; justify-content: center;
    color: var(--accent-red); font-weight: 900; font-size: 30px; line-height: 1.2;
    text-align: center;
  }
  .gift-badge svg { margin-bottom: 4px; }

  .invite {
    position: absolute; right: 30px; top: 945px;
    text-align: right; font-weight: 700; font-size: 28px; line-height: 42px;
  }

  .present-band {
    position: absolute; left: 0; right: 0; top: 1078px; height: 100px;
    background: var(--yellow);
    display: flex; align-items: center; justify-content: center;
    color: var(--accent-red); font-weight: 900; font-size: 54px; letter-spacing: -1px;
    white-space: nowrap;
  }
</style>
</head>
<body>
<main class="cover">
  <div class="cover-photo" role="img" aria-label="ピンクと青の背景に積み上がった木製ブロックの階段、それぞれに上向きの矢印があり、手が最上段のブロックを置いている写真"></div>

  <p class="tagline"><span class="hl">スル～っ</span><span class="small">と</span><span class="hl">トントン</span><span class="small">拍子に</span></p>
  <h1 class="title">ひらめく毎日!</h1>
  <p class="subtitle">をひらく本</p>

  <p class="lead">モヤモヤグルグルしてた<br>ただの主婦の私が、<br>まさかの<span class="hl">経営者</span>に<br>なった理由</p>
  <p class="author">森川遥香</p>

  <div class="gift-badge">
    <svg width="40" height="36" viewBox="0 0 40 36" aria-hidden="true">
      <rect x="4" y="14" width="32" height="20" fill="none" stroke="#f5c400" stroke-width="3"/>
      <rect x="2" y="9" width="36" height="7" fill="none" stroke="#f5c400" stroke-width="3"/>
      <line x1="20" y1="9" x2="20" y2="34" stroke="#f5c400" stroke-width="3"/>
      <path d="M20 9 C14 1 8 4 12 9 M20 9 C26 1 32 4 28 9" fill="none" stroke="#f5c400" stroke-width="3"/>
    </svg>
    <span>読者限定<br>プレゼント</span>
  </div>

  <p class="invite">「何かしたい」でも<br>「何をしたいのかわからない」<br>そんなあなたに</p>

  <p class="present-band">「星読みカルテ」プレゼント</p>
</main>
</body>
</html>
```